Blog Design for global news commentary

Need a very simple blog template (see attachment, Frontpage) that includes entries and ability to upload photos/video. Tabs are not needed (See Marlo Bistro Vermeil blog for sort of what I am going for but a lot less cluttered). A section that can access old entries is needed as well as a "contact me" tab. The format should be very simple. An entry and section for comments, new entry, section for comments etc. comments sections should be able to be monitored by me. With the ability for readers to contribute via coinlet. The look and feel should be sophisticated and should target an educated global audience. The blog is all about commenting on global news around the world. For example, a news article could be photographed and then commented on. Type face should be simple, clean and 1930's style. See Brindle Post magazine for looks and feel. If viewers wish to contribute they can make donations via coinlet on the site. Once the template is competed it should be very easy for me to update and work with and handed over to a web hosting service. I own the domain name which I want to use. It would be best to use an existing template eg wordpress. So in simple terms need a wordpress template adapted for this blog idea. Not sure what coded vs. uncoded means. But the overall objective is very simple. Template should be clean, no design elements other than the name of the blog.

Target Market(s)

Educated people from around the world interested in current events

Industry/Entity Type

News

Number of Pages Required

2 page

Other font styles liked:
• Upper East Side

Colors
0255a3
1b1b1b
5c5c5c

Requirements
Must have
• This is a blog so it should have all the standard features including daily updates, photo/video upload, comments that can be monitored by me, coinlet donation link. It should be easy for me to use and handle once completed and delivered to web host. It must have a simple, elegant look and feel. I have chose Serif font style but recommend a 1930's Art Deco - clean, unfussy type face. Type face Upper East Side is what I am looking for
Nice to have
• The look must be simple and no pictures, design elements or logos. Clean and crisp
Should not have
• Any pictures for illustrations as part of the overall design

```html
<!DOCTYPE html>
<html lang="en">
<head>
<meta charset="utf-8">
<title>Halvern — Global News Commentary</title>
<link rel="stylesheet" href="https://fonts.googleapis.com/css2?family=Poiret+One&family=Open+Sans:wght@400;600;700&display=swap">
<style>
:root{
  --blue:#0255a3;
  --ink:#1b1b1b;
  --grey:#5c5c5c;
  --page:#f1f1f1;
  --line:#dcdcdc;
  --white:#ffffff;
  --muted:#8a8a8a;
  --yellow:#f2c500;
  --foot-icon:#d4d4d4;
}
*{box-sizing:border-box;margin:0;padding:0}
html,body{width:1200px;height:2960px;overflow:hidden}
body{position:relative;background:var(--page);font-family:"Open Sans",Arial,sans-serif;color:var(--grey)}
.abs{position:absolute}

/* header */
.site-header{left:0;top:0;width:1200px;height:132px;background:var(--white)}
.contact-list{left:100px;top:28px;font-size:13px;line-height:22px;color:var(--grey)}
.contact-list span{display:flex;align-items:center;gap:8px}
.contact-list i{display:inline-block;width:10px;height:10px;background:var(--blue);border-radius:2px}
.brand{left:0;width:1200px;top:38px;text-align:center;font-family:"Poiret One",serif;font-size:44px;color:var(--blue);letter-spacing:1px}
.donate-btn{left:900px;top:40px;width:140px;height:46px;background:var(--blue);border-radius:4px;color:var(--white);font-weight:700;font-size:20px;display:flex;align-items:center;justify-content:center}
.search-btn{left:1058px;top:41px;width:44px;height:44px;border-radius:50%;background:#e7eef6;display:flex;align-items:center;justify-content:center}

.main-nav{left:0;top:132px;width:1200px;height:48px;background:var(--ink);display:flex;align-items:center;padding:0 100px;justify-content:space-between}
.main-nav a{color:#e8e8e8;text-decoration:none;font-size:15px;font-weight:600;letter-spacing:.5px}

.hero{left:0;top:180px;width:1200px;height:552px;background:linear-gradient(180deg,#3b3f45 0%,#6d6457 45%,#c8c2b6 75%,#4a4a4f 100%)}

/* posts */
.post-media{left:100px;width:652px}
.post-title{left:100px;width:652px;font-family:"Poiret One",serif;font-size:22px;font-weight:400;color:var(--ink);white-space:nowrap}
.post-excerpt{left:100px;width:652px;font-size:11.5px;line-height:19px;color:var(--grey)}
.post-meta{left:100px;font-size:12px;color:var(--muted);display:flex;gap:22px;align-items:center}
.post-meta b{color:var(--blue);font-weight:700;margin-right:4px}
.post-divider{left:100px;width:652px;height:1px;background:var(--line)}
.play{left:388px;top:1630px;width:76px;height:76px;border:3px solid rgba(255,255,255,.85);border-radius:50%;display:flex;align-items:center;justify-content:center}

.pagination{left:270px;top:2774px;width:310px;display:flex;justify-content:space-between;font-size:16px;color:var(--ink)}
.pagination .current{color:var(--blue);font-weight:700}

/* sidebar */
.widget{left:768px;width:332px;background:var(--white)}
.widget-head{height:60px;display:flex;align-items:center;justify-content:center;font-family:"Poiret One",serif;font-size:22px;color:var(--white)}
.head-blue{background:var(--blue)}
.head-dark{background:var(--grey)}
.cat-list{list-style:none;padding:16px 28px}
.cat-list li{font-size:12px;line-height:24.5px;color:var(--ink);display:flex;align-items:center;gap:8px;white-space:nowrap}
.cat-list li::before{content:"";width:5px;height:5px;background:var(--blue);border-radius:50%;flex:none}
.follow-text{padding:18px 40px 14px;text-align:center;font-size:12.5px;line-height:19px}
.social-row{display:flex;justify-content:center;gap:16px}
.social-row span{width:48px;height:48px;border-radius:50%;border:2px solid var(--blue);display:flex;align-items:center;justify-content:center}
.popular-item{display:flex;gap:14px;padding:0 20px;height:112px;align-items:center;border-bottom:1px solid #eee}
.popular-thumb{width:72px;height:72px;flex:none;background:linear-gradient(135deg,#7a6a5c,#c9b8a6)}
.popular-text{font-size:11.5px;line-height:17px;color:var(--grey)}
.popular-text small{display:block;font-size:10.5px;color:var(--blue);margin-top:4px}

.ad-box{left:768px;top:2292px;width:332px;height:236px;background:linear-gradient(180deg,#1f3b4d 0%,#2f5266 55%,#5b7380 100%);padding:30px 28px}
.ad-box strong{display:block;font-size:30px;font-weight:700;color:var(--yellow);line-height:32px}
.ad-box span{display:block;font-size:19px;font-weight:600;color:var(--white);margin-top:4px}

/* footer */
.site-footer{left:0;top:2828px;width:1200px;height:132px;background:var(--ink)}
.footer-social{left:0;width:1200px;top:2856px;display:flex;justify-content:center;gap:34px}
.footer-social span{width:24px;height:24px;display:flex;align-items:center;justify-content:center}
.footer-copy{left:0;width:1200px;top:2916px;text-align:center;font-size:11px;color:#8d8d8d}
</style>
</head>
<body>

<svg width="0" height="0" style="position:absolute">
  <defs>
    <symbol id="icon-mail" viewBox="0 0 24 24"><rect x="3" y="6" width="18" height="12" rx="1.5" fill="none" stroke="currentColor" stroke-width="2"/><path d="M3.5 7 L12 13 L20.5 7" fill="none" stroke="currentColor" stroke-width="2"/></symbol>
    <symbol id="icon-share" viewBox="0 0 24 24"><circle cx="6" cy="12" r="2.6" fill="currentColor"/><circle cx="18" cy="6" r="2.6" fill="currentColor"/><circle cx="18" cy="18" r="2.6" fill="currentColor"/><path d="M6 12 L18 6 M6 12 L18 18" stroke="currentColor" stroke-width="1.8"/></symbol>
    <symbol id="icon-chat" viewBox="0 0 24 24"><path d="M4 5 H20 V16 H10 L6 20 V16 H4 Z" fill="none" stroke="currentColor" stroke-width="2" stroke-linejoin="round"/></symbol>
    <symbol id="icon-globe" viewBox="0 0 24 24"><circle cx="12" cy="12" r="8.5" fill="none" stroke="currentColor" stroke-width="2"/><ellipse cx="12" cy="12" rx="3.8" ry="8.5" fill="none" stroke="currentColor" stroke-width="1.6"/><path d="M3.5 12 H20.5" stroke="currentColor" stroke-width="1.6"/></symbol>
    <symbol id="icon-play" viewBox="0 0 24 24"><rect x="3" y="5" width="18" height="14" rx="3" fill="none" stroke="currentColor" stroke-width="2"/><path d="M10 9 L15.5 12 L10 15 Z" fill="currentColor"/></symbol>
  </defs>
</svg>

<header class="abs site-header">
  <div class="abs contact-list">
    <span><i></i>info@halvernnews.com</span>
    <span><i></i>+00 5550 1234</span>
  </div>
  <div class="abs brand">Halvern</div>
  <div class="abs donate-btn">coinlet</div>
  <div class="abs search-btn">
    <svg width="20" height="20" viewBox="0 0 20 20"><circle cx="8" cy="8" r="6" fill="none" stroke="#0255a3" stroke-width="2.4"/><line x1="12.5" y1="12.5" x2="18" y2="18" stroke="#0255a3" stroke-width="2.6" stroke-linecap="round"/></svg>
  </div>
</header>

<nav class="abs main-nav">
  <a>NEWS</a><a>BLOG</a><a>CULTURE</a><a>BOOKS &amp; FICTION</a><a>SCIENCE</a><a>MAGAZINE</a><a>VIDEO</a><a>ARCHIVE</a><a>CONTACT</a>
</nav>

<div class="abs hero" role="img" aria-label="Photo of business people smiling around a meeting table"></div>

<!-- post 1 -->
<div class="abs post-media" style="top:812px;height:400px;background:linear-gradient(180deg,#f4f4f4 0%,#d9dde2 60%,#b9bfc6 100%)" role="img" aria-label="Photo of business people shaking hands in an office"></div>
<h2 class="abs post-title" style="top:1238px">The Complete Beginner's Guide to Choosing The Right Website</h2>
<p class="abs post-excerpt" style="top:1280px">There are many variations of passages of Lorem Ipsum available, but the majority have suffered alteration in some form, by injected humour, or randomised words which don't look even slightly believable. If you are going to use a passage of Lorem Ipsum, you need to be sure there isn't anything hidden in the middle of text. All the Lorem Ipsum generators on the Internet tend to repeat predefined chunks.</p>
<div class="abs post-meta" style="top:1376px"><span><b>BY</b>Ines Warrick</span><span><b>2207</b>views</span><span>Aug 07, 2016</span><span><b>3</b>Comments</span></div>
<div class="abs post-divider" style="top:1430px"></div>

<!-- post 2 -->
<div class="abs post-media" style="top:1472px;height:388px;background:linear-gradient(160deg,#2a2722 0%,#6b5a3e 50%,#c79a55 80%,#3a3228 100%)" role="img" aria-label="Video still of a cyclist riding at sunset"></div>
<div class="abs play"><svg width="26" height="30" viewBox="0 0 26 30"><path d="M4 3 L23 15 L4 27 Z" fill="none" stroke="#fff" stroke-width="3" stroke-linejoin="round"/></svg></div>
<h2 class="abs post-title" style="top:1902px">The Complete Beginner's Guide to Choosing The Right Website</h2>
<p class="abs post-excerpt" style="top:1944px">There are many variations of passages of Lorem Ipsum available, but the majority have suffered alteration in some form, by injected humour, or randomised words which don't look even slightly believable. If you are going to use a passage of Lorem Ipsum, you need to be sure there isn't anything hidden in the middle of text. All the Lorem Ipsum generators on the Internet tend to repeat predefined chunks.</p>
<div class="abs post-meta" style="top:2040px"><span><b>BY</b>Ines Warrick</span><span><b>2207</b>views</span><span>Aug 07, 2016</span><span><b>3</b>Comments</span></div>
<div class="abs post-divider" style="top:2100px"></div>

<!-- post 3 -->
<div class="abs post-media" style="top:2140px;height:380px;background:linear-gradient(180deg,#f2f2f2 0%,#e2e2e2 55%,#bdb3a8 100%)" role="img" aria-label="Photo of a smiling business team standing in a row"></div>
<h2 class="abs post-title" style="top:2560px">The Complete Beginner's Guide to Choosing The Right Website</h2>
<p class="abs post-excerpt" style="top:2602px">There are many variations of passages of Lorem Ipsum available, but the majority have suffered alteration in some form, by injected humour, or randomised words which don't look even slightly believable. If you are going to use a passage of Lorem Ipsum, you need to be sure there isn't anything hidden in the middle of text. All the Lorem Ipsum generators on the Internet tend to repeat predefined chunks.</p>
<div class="abs post-meta" style="top:2706px"><span><b>BY</b>Ines Warrick</span><span><b>2207</b>views</span><span>Aug 07, 2016</span><span><b>3</b>Comments</span></div>
<div class="abs post-divider" style="top:2752px"></div>

<div class="abs pagination"><span>‹</span><span class="current">1</span><span>2</span><span>3</span><span>4</span><span>5</span><span>6</span><span>›</span></div>

<!-- sidebar -->
<aside class="abs widget" style="top:812px;height:348px">
  <div class="widget-head head-blue">Categories</div>
  <ul class="cat-list">
    <li>Established fact that a reader will</li>
    <li>Distracted by the readable content of a page</li>
    <li>Looking at its layout: The point of using Lorem</li>
    <li>Layout is that it has a more-or-less Normal</li>
    <li>Distribution of letters, as opposed to Content</li>
    <li>Content here, making it look Like readable</li>
    <li>English. Many desktop</li>
    <li>Publishing packages and web page editors</li>
    <li>Lorem Ipsum as their default model</li>
    <li>And a search for 'lorem ipsum' will</li>
    <li>Uncover many websites</li>
  </ul>
</aside>

<aside class="abs widget" style="top:1296px;height:212px">
  <div class="widget-head head-dark">Follow Me</div>
  <p class="follow-text">There are many variations of passages of Lorem Ipsum available, but the majority have</p>
  <div class="social-row" style="color:var(--blue)">
    <span><svg width="20" height="20"><use href="#icon-mail"/></svg></span>
    <span><svg width="20" height="20"><use href="#icon-share"/></svg></span>
    <span><svg width="20" height="20"><use href="#icon-chat"/></svg></span>
    <span><svg width="20" height="20"><use href="#icon-globe"/></svg></span>
  </div>
</aside>

<aside class="abs widget" style="top:1568px;height:652px">
  <div class="widget-head head-blue">Most Popular</div>
  <div class="popular-item"><div class="popular-thumb" role="img" aria-label="Thumbnail portrait photo"></div><div class="popular-text">There are many variations of passages of Lorem Ipsum available, but the majority have suffered<small>2360 views · 3 Comments</small></div></div>
  <div class="popular-item"><div class="popular-thumb" role="img" aria-label="Thumbnail portrait photo"></div><div class="popular-text">There are many variations of passages of Lorem Ipsum available, but the majority have suffered<small>2360 views · 3 Comments</small></div></div>
  <div class="popular-item"><div class="popular-thumb" role="img" aria-label="Thumbnail portrait photo"></div><div class="popular-text">There are many variations of passages of Lorem Ipsum available, but the majority have suffered<small>2360 views · 3 Comments</small></div></div>
  <div class="popular-item"><div class="popular-thumb" role="img" aria-label="Thumbnail portrait photo"></div><div class="popular-text">There are many variations of passages of Lorem Ipsum available, but the majority have suffered<small>2360 views · 3 Comments</small></div></div>
  <div class="popular-item" style="border-bottom:0"><div class="popular-thumb" role="img" aria-label="Thumbnail portrait photo"></div><div class="popular-text">There are many variations of passages of Lorem Ipsum available, but the majority have suffered<small>2360 views · 3 Comments</small></div></div>
</aside>

<div class="abs ad-box" role="img" aria-label="Advertisement banner with a photo of palm trees">
  <strong>THERE ARE</strong>
  <span>MANY VARIATIONS OF</span>
</div>

<footer class="abs site-footer"></footer>
<div class="abs footer-social" style="color:var(--foot-icon)">
  <span><svg width="22" height="22"><use href="#icon-mail"/></svg></span>
  <span><svg width="22" height="22"><use href="#icon-share"/></svg></span>
  <span><svg width="22" height="22"><use href="#icon-chat"/></svg></span>
  <span><svg width="22" height="22"><use href="#icon-globe"/></svg></span>
  <span><svg width="22" height="22"><use href="#icon-play"/></svg></span>
</div>
<div class="abs footer-copy">Copyright © 2016 Halvern. All rights reserved.</div>

</body>
</html>
```